Trucking/service truck *Updated

Cards for a trucking company. Company transfers logs to saw mills. We are looking for something edgy, modern and fun. It's very limited when it comes to trucking business card choices. Plus the owner also runs an on-site service truck. He has 20+ years mechanic experience.
Colors are open. Favorites are orange & purple, but not must have. We really want to emphasize trust, dependability and knowledge with a bright, attention getter.
On card:
Hallowell & Hallowell
Dean Hallowell - Owner/Manager/Maintenance 903-512-4097
Marla Hallowell -Office Administration/Bookkeeping 903-627-1954
4718 Juniper Ln.
Gilmer, Texas 75392
903-659-3021 - Office
Updates
Just a thought. Do you think you can combine the Taurus and Pisces signs? And put in the corner, or on the back or anything really? Thanks! You all or doing fantastic!
Industry/Entity Type
Business
Colors
Designer to choose colors to be used in the design.
Look and feel
Each slider illustrates characteristics of the customer's brand and the style your logo design should communicate.

```html
<!DOCTYPE html>
<html lang="en">
<head>
<meta charset="utf-8">
<title>Hallowell &amp; Hallowell — Business Cards</title>
<link rel="stylesheet" href="https://fonts.googleapis.com/css2?family=Exo+2:wght@400;500;700&display=swap">
<style>
  :root {
    --backdrop: #8f8f8f;
    --card: #ffffff;
    --panel-dark: #123c8c;
    --panel-mid: #2a62c4;
    --panel-light: #3f7fe0;
    --divider: rgba(255,255,255,0.75);
    --accent-red: #ee1c0c;
    --band-dark: #333333;
    --name-red: #9b2f24;
    --ink: #2e2e2e;
    --brand-blue: #1d3f8a;
  }
  html, body {
    margin: 0;
    width: 1200px;
    height: 894px;
    overflow: hidden;
    background: var(--backdrop);
    font-family: "Exo 2", sans-serif;
  }
  .card {
    position: absolute;
    width: 620px;
    height: 354px;
    background: var(--card);
    box-shadow: 0 10px 24px rgba(0,0,0,0.3);
    overflow: hidden;
  }
  .card-back { left: 540px; top: 40px; }
  .card-front { left: 40px; top: 480px; }

  /* back side */
  .back-band {
    position: absolute;
    right: 0;
    top: 62px;
    width: 150px;
    height: 44px;
    background: var(--band-dark);
  }
  .back-brand {
    position: absolute;
    left: 0;
    right: 0;
    top: 150px;
    display: flex;
    justify-content: center;
    align-items: center;
    gap: 14px;
  }
  .back-brand .brand-dot { width: 40px; height: 40px; }
  .back-brand .brand-name { font-size: 24px; }

  /* shared brand */
  .brand-dot {
    border-radius: 50%;
    background: var(--brand-blue);
    flex: none;
  }
  .brand-name {
    font-weight: 500;
    color: var(--brand-blue);
    white-space: nowrap;
  }

  /* front side */
  .front-brand {
    position: absolute;
    left: 28px;
    top: 26px;
    display: flex;
    align-items: center;
    gap: 10px;
  }
  .front-brand .brand-dot { width: 30px; height: 30px; }
  .front-brand .brand-name { font-size: 19px; }
  .accent-bar {
    position: absolute;
    right: 0;
    top: 92px;
    width: 190px;
    height: 24px;
    background: var(--accent-red);
  }
  .person {
    position: absolute;
    left: 248px;
    top: 122px;
  }
  .person-name {
    margin: 0;
    font-size: 27px;
    font-weight: 700;
    letter-spacing: 1px;
    text-transform: uppercase;
    line-height: 1;
    white-space: nowrap;
  }
  .person-name .first { color: var(--name-red); }
  .person-name .last { color: var(--ink); }
  .person-title {
    margin: 4px 0 0;
    font-size: 14px;
    font-weight: 500;
    letter-spacing: 1px;
    text-transform: uppercase;
    color: var(--ink);
    white-space: nowrap;
  }
  .contact-panel {
    position: absolute;
    left: 27px;
    top: 184px;
    width: 545px;
    height: 148px;
    border-radius: 14px;
    background: radial-gradient(ellipse at 50% 40%, var(--panel-light), var(--panel-mid) 45%, var(--panel-dark));
    display: grid;
    grid-template-columns: 1fr 1fr 1fr;
  }
  .contact-item {
    display: flex;
    flex-direction: column;
    align-items: center;
    justify-content: center;
    gap: 10px;
    color: #fff;
    font-size: 13px;
    line-height: 1.4;
    text-align: center;
    letter-spacing: 0.3px;
    white-space: nowrap;
  }
  .contact-item + .contact-item { border-left: 1.5px solid var(--divider); }
  .contact-icon { width: 30px; height: 30px; }
</style>
</head>
<body>
  <section class="card card-back" aria-label="Card back">
    <div class="back-band"></div>
    <div class="back-brand">
      <span class="brand-dot"></span>
      <span class="brand-name">Hallowell &amp; Hallowell</span>
    </div>
  </section>

  <main class="card card-front">
    <div class="front-brand">
      <span class="brand-dot"></span>
      <span class="brand-name">Hallowell &amp; Hallowell</span>
    </div>

    <div class="accent-bar"></div>

    <div class="person">
      <h1 class="person-name"><span class="first">Dean</span> <span class="last">Hallowell</span></h1>
      <p class="person-title">Owner / Manager / Maintenance</p>
    </div>

    <section class="contact-panel">
      <div class="contact-item">
        <svg class="contact-icon" viewBox="0 0 48 48" aria-hidden="true">
          <path d="M8 18c0-6 7-9 16-9s16 3 16 9v3h-8v-4c-2-1-5-1.5-8-1.5s-6 .5-8 1.5v4H8z" fill="#fff"/>
          <path d="M14 24h20l6 14H8z" fill="#fff"/>
          <circle cx="24" cy="31" r="4" fill="var(--panel-mid)"/>
        </svg>
        <div>903-512-4097<br>903-659-3021</div>
      </div>
      <div class="contact-item">
        <svg class="contact-icon" viewBox="0 0 48 48" aria-hidden="true" fill="none" stroke="#fff" stroke-width="2.5">
          <circle cx="24" cy="24" r="17"/>
          <ellipse cx="24" cy="24" rx="7" ry="17"/>
          <line x1="7" y1="24" x2="41" y2="24"/>
          <path d="M10 15h28M10 33h28"/>
        </svg>
        <div>info@hallowellhaul.com<br>www.hallowellhaul.com</div>
      </div>
      <div class="contact-item">
        <svg class="contact-icon" viewBox="0 0 48 48" aria-hidden="true">
          <path d="M24 4c-8 0-14 6-14 14 0 10 14 26 14 26s14-16 14-26c0-8-6-14-14-14z" fill="#fff"/>
          <circle cx="24" cy="18" r="5" fill="var(--panel-mid)"/>
        </svg>
        <div>4718 Juniper Ln.<br>Gilmer, Texas 75392</div>
      </div>
    </section>
  </main>
</body>
</html>
```